Bref créative
The Marlowe Gala
Event Planning
Professional
Rosalind Hartwell
Owner - The Marlowe Gala
4105 - 27 Ashcombe Avenue
Toronto, ON M5R 2K7
rosalind@TheMarloweGala.example
www.TheMarloweGala.example
The card can be single or double sided i don't mind. Just be creative and make it clean!!!
Thanks!
It can be single or double sided I dont mind.

```html
<!DOCTYPE html>
<html lang="en">
<head>
<meta charset="utf-8">
<title>The Marlowe Gala – Business Card</title>
<link href="https://fonts.googleapis.com/css2?family=Raleway:wght@300;400;600&display=swap" rel="stylesheet">
<style>
  :root {
    --backdrop: #e9e7e4;
    --card: #ffffff;
    --ink: #3b3b3b;
    --ink-soft: #777777;
    --band-dark: #4a4a4a;
    --band-mid: #8c8c8c;
    --band-light: #c9c9c9;
    --rule: #9a9a9a;
  }
  * { box-sizing: border-box; margin: 0; padding: 0; }
  html, body {
    width: 1200px; height: 629px; overflow: hidden;
    background: var(--backdrop);
    font-family: "Raleway", Arial, sans-serif;
    color: var(--ink);
  }
  .stage {
    width: 1200px; height: 629px;
    display: flex; align-items: center; justify-content: center; gap: 60px;
  }
  .card {
    position: relative;
    width: 500px; height: 286px;
    background: var(--card);
    box-shadow: 0 6px 18px rgba(0,0,0,0.15);
    overflow: hidden;
  }
  /* Wordmark */
  .wordmark {
    position: absolute;
    display: flex; flex-direction: column; align-items: center;
  }
  .wordmark-square {
    width: 46px; height: 46px; background: var(--ink); margin-bottom: 12px;
  }
  .wordmark-name {
    font-weight: 400; font-size: 19px; letter-spacing: 3px;
    text-transform: uppercase; color: var(--ink); white-space: nowrap;
  }
  .wordmark-tagline {
    margin-top: 5px; padding-top: 4px;
    border-top: 1px solid var(--rule);
    font-weight: 300; font-size: 10px; letter-spacing: 3px;
    color: var(--ink-soft); text-transform: lowercase;
  }
  .card-front .wordmark { left: 0; right: 0; top: 88px; }

  /* Back side */
  .swoosh { position: absolute; top: 0; left: 0; }
  .card-back .wordmark { left: 34px; top: 104px; align-items: center; }
  .card-back .wordmark-square { width: 38px; height: 38px; margin-bottom: 10px; }
  .card-back .wordmark-name { font-size: 14px; letter-spacing: 2px; }
  .card-back .wordmark-tagline { font-size: 8px; letter-spacing: 2.5px; }

  .holder {
    position: absolute; right: 28px; top: 150px; text-align: right;
  }
  .holder-name { font-weight: 600; font-size: 12px; color: var(--ink); }
  .holder-role { font-weight: 400; font-size: 9px; color: var(--ink-soft); margin-top: 3px; }

  .contact-list {
    position: absolute; left: 34px; bottom: 16px;
    list-style: none; font-size: 8px; color: var(--ink); line-height: 1;
  }
  .contact-item { display: flex; align-items: center; gap: 6px; margin-top: 4px; }
  .contact-icon {
    width: 10px; height: 10px; border-radius: 50%;
    background: var(--ink); flex: none;
    display: flex; align-items: center; justify-content: center;
  }
</style>
</head>
<body>
<main class="stage">
  <section class="card card-front" aria-label="Card front">
    <div class="wordmark">
      <div class="wordmark-square"></div>
      <div class="wordmark-name">The Marlowe Gala</div>
      <div class="wordmark-tagline">event planning</div>
    </div>
  </section>

  <section class="card card-back" aria-label="Card back">
    <svg class="swoosh" width="500" height="286" viewBox="0 0 500 286" aria-hidden="true">
      <path d="M0 0 H500 V40 C360 40 200 70 0 130 Z" fill="var(--band-light)"/>
      <path d="M0 0 H500 V28 C350 30 190 58 0 112 Z" fill="var(--band-mid)"/>
      <path d="M120 0 H500 V24 C380 22 260 30 120 60 C60 72 20 86 0 96 V0 Z" fill="var(--band-dark)"/>
    </svg>

    <div class="wordmark">
      <div class="wordmark-square"></div>
      <div class="wordmark-name">The Marlowe Gala</div>
      <div class="wordmark-tagline">event planning</div>
    </div>

    <div class="holder">
      <div class="holder-name">Rosalind Hartwell</div>
      <div class="holder-role">Owner - The Marlowe Gala</div>
    </div>

    <ul class="contact-list">
      <li class="contact-item">
        <span class="contact-icon"><svg width="6" height="7" viewBox="0 0 6 7"><path d="M3 0a2.2 2.2 0 0 0-2.2 2.2C.8 3.8 3 7 3 7s2.2-3.2 2.2-4.8A2.2 2.2 0 0 0 3 0z" fill="#fff"/></svg></span>
        4105 - 27 Ashcombe Avenue, Toronto, ON M5R 2K7
      </li>
      <li class="contact-item">
        <span class="contact-icon"><svg width="6" height="6" viewBox="0 0 6 6"><path d="M1 0h1.4l.6 1.6-.9.7a3.6 3.6 0 0 0 1.6 1.6l.7-.9L6 3.6V5a1 1 0 0 1-1 1A5 5 0 0 1 0 1a1 1 0 0 1 1-1z" fill="#fff"/></svg></span>
        416 555 0142
      </li>
      <li class="contact-item">
        <span class="contact-icon"><svg width="6" height="6" viewBox="0 0 6 6"><path d="M1 0h1.4l.6 1.6-.9.7a3.6 3.6 0 0 0 1.6 1.6l.7-.9L6 3.6V5a1 1 0 0 1-1 1A5 5 0 0 1 0 1a1 1 0 0 1 1-1z" fill="#fff"/></svg></span>
        416 555 0187
      </li>
      <li class="contact-item">
        <span class="contact-icon"><svg width="6" height="5" viewBox="0 0 6 5"><rect x="0" y="0" width="6" height="5" fill="#fff"/><path d="M0 0l3 2.6L6 0" stroke="var(--ink)" stroke-width=".7" fill="none"/></svg></span>
        rosalind@TheMarloweGala.example
      </li>
      <li class="contact-item">
        <span class="contact-icon"><svg width="6" height="6" viewBox="0 0 6 6"><circle cx="3" cy="3" r="2.6" stroke="#fff" stroke-width=".7" fill="none"/><path d="M.4 3h5.2M3 .4c1.4 1.5 1.4 3.7 0 5.2M3 .4c-1.4 1.5-1.4 3.7 0 5.2" stroke="#fff" stroke-width=".5" fill="none"/></svg></span>
        www.TheMarloweGala.example
      </li>
    </ul>
  </section>
</main>
</body>
</html>
```